Business Card Design

The image I attached was a quick thought to my design. I have triplets and was invisioning something with three figures with maybe the colors blue, pink and green. I would like it to look very chic and modern yet soothing/healing. I will take any fresh ideas as well.

Side 1: Contact Details
Side 2: Appointment section (mandatory)
Updates

Thank u all for your preliminary designs. I had sent the old design over and am looking for a bold fresh NEW LOOK  for CORE MOTION. I saw some really creative ideas in the gallery. If you have any other questions please feel free to email me at rtbwakes@quellmail.net.

Thanks

Please keep in mind that it is mandatory that on the back of the card is for appointments.

Thank you.

Reason: The two mandatory elements that need to be on the card is that her title needs to read as so:

Reason: The criteria is still not being met. Her title needs to read as so: Dr. Marisa Kettner, P.T., D.P.T. Doctor of Physical Therapy and The appointment info must go on the BACK of the card. Looking forward to some more great designs. Thanks.

Industry/Entity Type

Business

Contact Information for Business Card

Core Motion
Physical & Aquatic Therapy
Dr. Marisa Kettner, P.T., D.P.T.
Doctor of Physical Therapy

22-48 B Birchwick Lane
Elmbury, N.Y. 11592
(Located inside of the Summit gym in the Pinecrest shopping center)

Phone & Fax: (631) 555-0172
Mkettner4@harbornet.net

Requirements
Must have
• One the back I would like to do an appointment layout.

```html
<!DOCTYPE html>
<html lang="en">
<head>
<meta charset="utf-8">
<title>Core Motion – Business Card</title>
<link rel="stylesheet" href="https://fonts.googleapis.com/css2?family=Arimo:wght@400;700&family=Questrial&display=swap">
<style>
  :root {
    --stage: #d4d4d4;
    --paper: #fbfbfb;
    --green: #7cbc1f;
    --green-text: #7aba22;
    --ink: #1b1b1b;
    --rule: #2a2a2a;
  }
  * { box-sizing: border-box; margin: 0; padding: 0; }
  html, body { width: 1200px; height: 787px; overflow: hidden; }
  body {
    background: var(--stage);
    font-family: "Arimo", Arial, sans-serif;
    color: var(--ink);
    position: relative;
  }
  .card {
    position: absolute;
    top: 233px;
    width: 560px;
    height: 320px;
    background: var(--paper);
    box-shadow: 0 4px 14px rgba(0,0,0,.18);
    overflow: hidden;
  }
  .card--front { left: 27px; }
  .card--back { left: 613px; }

  /* front */
  .edge-bar { position: absolute; top: 0; bottom: 0; width: 14px; background: var(--green); }
  .edge-bar--left { left: 0; }
  .edge-bar--right { right: 0; }
  .logo-slot {
    position: absolute; left: 62px; top: 32px; width: 90px;
    text-align: center; font-size: 12px; line-height: 19px; font-weight: 700;
    font-family: "Questrial", sans-serif; color: #333;
  }
  .brand { position: absolute; left: 240px; top: 26px; font-family: "Questrial", sans-serif; }
  .brand__name { font-size: 27px; font-weight: 700; letter-spacing: .5px; -webkit-text-stroke: .6px var(--ink); line-height: 30px; }
  .brand__tagline { font-size: 15.5px; font-weight: 700; -webkit-text-stroke: .3px var(--ink); letter-spacing: .2px; padding-left: 2px; }
  .person { position: absolute; left: 34px; top: 108px; }
  .person__name { color: var(--green-text); font-size: 19px; font-weight: 700; }
  .person__creds { font-size: 8px; font-weight: 700; margin-left: 3px; }
  .person__title { font-size: 11px; font-weight: 700; margin: 3px 0 0 82px; }
  .location-note {
    position: absolute; right: 30px; top: 166px;
    font-family: "Questrial", sans-serif; font-size: 13px; font-weight: 700;
  }
  .divider { position: absolute; left: 14px; right: 14px; top: 194px; height: 2px; background: var(--green); }
  .contact-phone {
    position: absolute; left: 0; right: 0; top: 206px; text-align: center;
    font-size: 12.5px; font-weight: 700;
  }
  .contact-phone__label { color: var(--green-text); }
  .contact-address { position: absolute; left: 30px; top: 236px; display: flex; gap: 9px; font-size: 13px; font-weight: 700; line-height: 18px; }
  .contact-email { position: absolute; left: 322px; top: 250px; display: flex; gap: 10px; align-items: center; font-size: 13px; font-weight: 700; }
  .icon { flex: none; }

  /* back */
  .edge-band { position: absolute; left: 0; right: 0; height: 14px; background: var(--green); }
  .edge-band--top { top: 0; }
  .edge-band--bottom { bottom: 0; }
  .appointments__label { position: absolute; left: 28px; top: 58px; font-size: 11px; font-weight: 700; }
  .appointments__line { position: absolute; left: 28px; right: 24px; border-top: 1.5px dashed var(--rule); }
</style>
</head>
<body>
  <section class="card card--front" aria-label="Card front">
    <div class="edge-bar edge-bar--left"></div>
    <div class="edge-bar edge-bar--right"></div>

    <div class="logo-slot">Your Logo<br>Here</div>

    <header class="brand">
      <div class="brand__name">CORE MOTION</div>
      <div class="brand__tagline">PHYSICAL &amp; AQUATIC THERAPY</div>
    </header>

    <div class="person">
      <div><span class="person__name">Dr. Marisa Kettner</span><span class="person__creds">P.T., D.P.T.</span></div>
      <div class="person__title">Doctor of Physical Therapy</div>
    </div>

    <p class="location-note">( Located inside of the Summit gym in the Pinecrest shopping center )</p>

    <div class="divider"></div>

    <p class="contact-phone"><span class="contact-phone__label">Phone &amp; Fax:</span> (631) 555-0172</p>

    <div class="contact-address">
      <svg class="icon" width="11" height="15" viewBox="0 0 11 15" aria-hidden="true">
        <path d="M5.5 0.5a5 5 0 0 0-5 5c0 3.6 5 9 5 9s5-5.4 5-9a5 5 0 0 0-5-5z" fill="var(--green)"/>
        <circle cx="5.5" cy="5.5" r="2" fill="var(--paper)"/>
      </svg>
      <address style="font-style:normal">22-48 B Birchwick Lane<br>Elmbury, N.Y. 11592.</address>
    </div>

    <div class="contact-email">
      <svg class="icon" width="18" height="13" viewBox="0 0 18 13" aria-hidden="true">
        <rect x="0" y="0" width="18" height="13" fill="var(--green)"/>
        <path d="M1 1l8 6 8-6" stroke="var(--paper)" stroke-width="1.5" fill="none"/>
      </svg>
      <span>Mkettner4@harbornet.net</span>
    </div>
  </section>

  <section class="card card--back" aria-label="Card back">
    <div class="edge-band edge-band--top"></div>
    <div class="edge-band edge-band--bottom"></div>
    <p class="appointments__label">Appointments:</p>
    <div class="appointments__line" style="top:82px"></div>
    <div class="appointments__line" style="top:124px"></div>
    <div class="appointments__line" style="top:166px"></div>
    <div class="appointments__line" style="top:208px"></div>
    <div class="appointments__line" style="top:250px"></div>
  </section>
</body>
</html>
```